Need UI Design for HRIS/Company Employee Portal

Currently have a custom built system that we hire and use as our employee database and employee portal for everyone in our company. The software has evolved dramatically and needs to be completely user friendly and aesthetically pleasing. Attached are a few ideas and pages we already have. Please make 5 designs for the 5 different pages below. Would need all specifications of content used, color code, font/typography, icons used, etc. We can pretty much pull any information from anywhere we have for example, employee photo, address, DOB, Hire date, Title, ETC.

-Company Staff/Admin Welcome Page
- We want quick shortcuts/buttons or icons for staff functions, such as terminate, hire, information change, reports, etc
-Employee Profile Welcome Page
- We want quick shortcuts/buttons or icons for direct deposit, time off request, information change, pay stubs
-List of Applications/Candidates Page
-Profile Search Page
-Manage Inventory

Target Market(s)

Employees

Industry/Entity Type

It Company

Coding

Coded - Design and coding required

Number of Pages Required

5+ page

Font styles to use
Sans Serif

Requirements
Must have
• Must be professional! Aesthetics, Icons, Easy User Interface, Modern New technology look, can be responsive to mobile
Should not have
• Nothing old school

```html
<!DOCTYPE html>
<html lang="en">
<head>
<meta charset="utf-8">
<title>Employee Portal – Profile</title>
<link rel="stylesheet" href="https://fonts.googleapis.com/css2?family=Open+Sans:wght@400;600;700&display=swap">
<style>
  :root{
    --ink:#111111;
    --text:#333333;
    --muted:#6b6b6b;
    --faint:#a8a8a8;
    --page:#f3f3f3;
    --card:#ffffff;
    --nav:#000000;
    --accent:#f0c230;
    --brand:#3d52b5;
    --line:#e2e2e2;
  }
  *{box-sizing:border-box;margin:0;padding:0}
  html,body{width:1200px;height:885px;overflow:hidden}
  body{font-family:"Open Sans",Arial,sans-serif;background:var(--page);color:var(--text);position:relative}

  .site-header{height:127px;background:var(--card);position:relative}
  .brand{position:absolute;left:125px;top:50px;display:flex;align-items:center;gap:10px}
  .brand-mark{width:22px;height:22px;background:var(--brand)}
  .brand-name{font-size:13px;font-weight:700;color:var(--brand);letter-spacing:.5px}
  .user{position:absolute;right:125px;top:39px;display:flex;align-items:center;gap:13px;font-size:12px;color:var(--muted)}
  .avatar{width:50px;height:50px;border-radius:50%;background:radial-gradient(circle at 50% 40%,#b89a82,#5a4a3e)}

  .main-nav{height:42px;background:var(--nav);display:flex;padding-left:125px;gap:32px}
  .main-nav a{color:#fff;text-decoration:none;font-size:12px;line-height:42px;position:relative;letter-spacing:.2px}
  .main-nav a.current::after{content:"";position:absolute;left:0;right:0;bottom:0;height:3px;background:var(--accent)}

  .card{background:var(--card);box-shadow:0 1px 3px rgba(0,0,0,.18);position:absolute}
  .profile{left:125px;top:194px;width:707px;height:300px}
  .profile-photo{position:absolute;left:8px;top:8px;width:292px;height:284px;background:linear-gradient(135deg,#cfc4b6,#efe9e2 60%,#d9d2c8)}
  .profile-info{position:absolute;left:325px;top:28px}
  .profile-name{font-size:21px;font-weight:700;color:var(--ink)}
  .profile-hired{font-size:13.5px;color:var(--ink);margin-top:4px}
  .divider{width:25px;height:1px;background:var(--line);margin:19px 0 20px}
  .fields{list-style:none;font-size:12px;color:var(--muted)}
  .fields li{line-height:23.3px}
  .fields b{font-weight:700;color:#555}

  .status{left:856px;top:194px;width:219px;height:300px;padding:28px 25px 0}
  .status-title{font-size:21px;font-weight:600;color:var(--brand);display:flex;justify-content:space-between;align-items:center}
  .status-list{list-style:none;font-size:10px;color:var(--muted);line-height:15px}
  .status-list b{color:#555}
  .status-list.first{margin-top:1px}
  .status-list.second{margin-top:26px}
  .rehire{display:block;margin-top:24px;height:33px;width:169px;background:var(--brand);color:#fff;border:0;font:600 11px "Open Sans",sans-serif;letter-spacing:.5px}

  .feature{top:519px;width:300px;height:275px}
  .feature .art{height:200px}
  .feature h3{font-size:15px;font-weight:400;color:var(--ink);margin:20px 17px 0}
  .feature p{font-size:12px;color:var(--muted);margin:4px 17px 0}
  .f1{left:125px}.f1 .art{background:linear-gradient(135deg,#d8d4c6,#4b4c52 70%,#2a2f44)}
  .f2{left:450px}.f2 .art{background:linear-gradient(180deg,#c9c2b0,#7b6b57 55%,#3a2a22)}
  .f3{left:775px}.f3 .art{background:linear-gradient(180deg,#3b3f4a,#1a1c22 60%,#0d0e12)}

  .site-footer{position:absolute;left:125px;right:125px;top:819px;border-top:1px solid var(--line);padding-top:25px;display:flex;justify-content:space-between;font-size:11.5px;color:var(--faint)}
</style>
</head>
<body>
  <header class="site-header">
    <div class="brand"><span class="brand-mark"></span><span class="brand-name">NORTHWALL PATROL SERVICES, INC.</span></div>
    <div class="user">Paul Harmon <span class="avatar" role="img" aria-label="Signed-in user portrait"></span></div>
  </header>
  <nav class="main-nav">
    <a class="current" href="#">HOME</a>
    <a href="#">PERSONAL LICENSES</a>
    <a href="#">FORMS/REQUESTS</a>
    <a href="#">TEAM CONTACTS</a>
    <a href="#">BENEFITS</a>
    <a href="#">TRAINING</a>
    <a href="#">EQUIPMENT</a>
    <a href="#">HELP</a>
  </nav>

  <section class="card profile">
    <div class="profile-photo" role="img" aria-label="Employee portrait photo"></div>
    <div class="profile-info">
      <h1 class="profile-name">Daniel Reyes</h1>
      <p class="profile-hired">Hired on 21st Aug 2008 &nbsp;·&nbsp; 17 years</p>
      <div class="divider"></div>
      <ul class="fields">
        <li><b>Address:</b> 42 Willow Bend Apt. 118</li>
        <li><b>City:</b> Harlow</li>
        <li><b>Zip:</b> 480-312</li>
        <li><b>Phone:</b> +912 - 55501234</li>
        <li><b>Cell Phone:</b> +91 - 9000555123</li>
        <li><b>Email:</b> officer.daniel.reyes@example.com</li>
      </ul>
    </div>
  </section>

  <aside class="card status">
    <div class="status-title">Active
      <svg width="16" height="12" viewBox="0 0 16 12" aria-hidden="true"><path d="M1 6l4.5 4.5L15 1" fill="none" stroke="#3d52b5" stroke-width="2"/></svg>
    </div>
    <ul class="status-list first">
      <li><b>Card Number:</b> 9890-2324</li>
      <li><b>Card Expiry Date:</b> 28th Oct 2020</li>
    </ul>
    <ul class="status-list second">
      <li><b>SSN:</b> XXXX-0883</li>
      <li><b>Twic Card Number:</b> &nbsp;132-234-3256</li>
      <li><b>ID &nbsp;Type:</b> State ID</li>
      <li><b>ID No:</b> 3256-883-132-234</li>
      <li><b>ID Expiry Date:</b> 14th Jan 2018</li>
      <li><b>Pin No:</b> 89772</li>
      <li><b>Reports To:</b> Mesa Ridge, AZ</li>
    </ul>
    <button class="rehire">RE - HIRE</button>
  </aside>

  <article class="card feature f1">
    <div class="art" role="img" aria-label="Patrol officers standing beside service vans"></div>
    <h3>Efficient &amp; Cost Effective Services</h3>
    <p>Emergency Crisis &amp; Response Teams</p>
  </article>
  <article class="card feature f2">
    <div class="art" role="img" aria-label="Officers in a training session around a conference table"></div>
    <h3>NPS Careers &amp; Training</h3>
    <p>Become a Certified Security Officer</p>
  </article>
  <article class="card feature f3">
    <div class="art" role="img" aria-label="Video surveillance control room with monitor wall"></div>
    <h3>Video Surveillance &amp; Support</h3>
    <p>Complete Support &amp; Alarm Verification</p>
  </article>

  <footer class="site-footer">
    <span>Copyright © 1997-2015. Northwall Patrol Services, Inc. All Rights Reserved.</span>
    <span>Privacy Policy</span>
  </footer>
</body>
</html>
```